The name of the company is Kestrel Rehab buying foreclosed homes and remodeling

A sleek classy card. It’s a home remodel and house flip company. Something mostly black with dark gray and red in color . Something with two f”s as a logo on front as shown in pictures. Kind of just let you guys run with it . I left a few pictures that should help
You guys get an idea of what I thought was good also left all the information for back of the card

Target Market(s)

Home remodel consumers

Industry/Entity Type

Construction Company

Contact Information for Business Card

All details are on photo

Font styles to use
Decorative

Colors

Designer to choose colors to be used in the design.

Requirements
Must have
• Name of company on front. Kestrel Rehab
Nice to have
• Up to you guys I trust you
Should not have
• Not sure

```html
<!DOCTYPE html>
<html lang="en">
<head>
<meta charset="utf-8">
<title>Daniel Ashcombe – Kestrel Rehab</title>
<link rel="stylesheet" href="https://fonts.googleapis.com/css2?family=Bebas+Neue&family=Open+Sans:wght@400&display=swap">
<style>
  :root {
    --ink: #000000;
    --charcoal: #555555;
    --paper: #ffffff;
    --red-bright: #e00d0d;
    --red-deep: #5e0000;
    --mail-gray: #c6c6c6;
    --mail-red: #d8463a;
    --social-red: #e33a5c;
    --globe-blue: #2a7fbf;
    --text: #111111;
  }
  * { margin: 0; padding: 0; box-sizing: border-box; }
  html, body { width: 1200px; height: 777px; overflow: hidden; background: var(--ink); }
  .card { position: relative; width: 1200px; height: 777px; overflow: hidden; font-family: "Open Sans", sans-serif; }
  .card-shapes { position: absolute; inset: 0; width: 1200px; height: 777px; }
  .holder-name {
    position: absolute; left: 24px; top: 10px;
    font-family: "Bebas Neue", sans-serif; font-size: 104px; line-height: 1;
    letter-spacing: 2px; color: var(--paper); white-space: nowrap;
  }
  .contact-icons { position: absolute; left: 100px; top: 197px; width: 84px; }
  .contact-icons svg { display: block; width: 84px; height: 84px; margin-bottom: -4px; }
  .contact-divider { position: absolute; left: 224px; top: 209px; width: 4px; height: 313px; background: var(--ink); }
  .contact-list { position: absolute; left: 265px; top: 0; list-style: none; color: var(--text); }
  .contact-item { position: absolute; left: 0; white-space: nowrap; font-size: 38px; line-height: 1; }
  .contact-email { top: 222px; font-size: 41px; }
  .contact-handle { top: 307px; }
  .contact-web { top: 391px; }
  .contact-phone { top: 474px; }
  .services { position: absolute; left: 0; top: 0; list-style: none; color: var(--paper); }
  .service {
    position: absolute; white-space: nowrap; font-size: 44px; line-height: 1;
    padding-left: 45px;
  }
  .service::before {
    content: ""; position: absolute; left: 0; top: 50%; width: 24px; height: 24px;
    margin-top: -10px; border-radius: 50%; background: var(--paper);
  }
  .service-a { left: 143px; top: 664px; }
  .service-b { left: 572px; top: 664px; }
  .service-c { left: 143px; top: 724px; }
  .service-d { left: 572px; top: 724px; }
</style>
</head>
<body>
<main class="card">
  <svg class="card-shapes" viewBox="0 0 1004 650" preserveAspectRatio="none" aria-hidden="true">
    <defs>
      <linearGradient id="band-top" x1="0" y1="0" x2="0" y2="1">
        <stop offset="0" stop-color="var(--charcoal)"/>
        <stop offset="0.45" stop-color="var(--ink)"/>
      </linearGradient>
      <linearGradient id="band-bottom" x1="0" y1="0" x2="0" y2="1">
        <stop offset="0.6" stop-color="var(--ink)"/>
        <stop offset="1" stop-color="#2e2e2e"/>
      </linearGradient>
      <linearGradient id="wedge-right" x1="0" y1="0" x2="1" y2="0">
        <stop offset="0" stop-color="var(--red-bright)"/>
        <stop offset="1" stop-color="var(--red-deep)"/>
      </linearGradient>
      <linearGradient id="wedge-left" x1="1" y1="0" x2="0" y2="0">
        <stop offset="0" stop-color="var(--red-bright)"/>
        <stop offset="1" stop-color="var(--red-deep)"/>
      </linearGradient>
    </defs>
    <rect class="band-top" x="0" y="0" width="1004" height="300" fill="url(#band-top)"/>
    <rect class="band-bottom" x="0" y="300" width="1004" height="350" fill="url(#band-bottom)"/>
    <polygon class="wedge-right" points="615,104 1004,140 1004,255" fill="url(#wedge-right)"/>
    <polygon class="wedge-left" points="0,423 290,547 0,500" fill="url(#wedge-left)"/>
    <polygon class="panel" points="0,138 615,104 1004,255 1004,495 290,547 0,423" fill="var(--paper)"/>
  </svg>

  <h1 class="holder-name">Daniel Ashcombe</h1>

  <div class="contact-icons" aria-hidden="true">
    <svg viewBox="0 0 84 84"><rect x="8" y="16" width="68" height="52" rx="4" fill="var(--mail-gray)"/></svg>
    <svg viewBox="0 0 84 84"><circle cx="42" cy="42" r="32" fill="var(--social-red)"/></svg>
    <svg viewBox="0 0 84 84" fill="none" stroke="var(--globe-blue)" stroke-width="5">
      <circle cx="42" cy="42" r="34"/>
      <ellipse cx="42" cy="42" rx="15" ry="34"/>
      <line x1="42" y1="8" x2="42" y2="76"/>
      <line x1="8" y1="42" x2="76" y2="42"/>
      <path d="M14 24 H70 M14 60 H70"/>
    </svg>
    <svg viewBox="0 0 84 84">
      <circle cx="42" cy="42" r="32" fill="none" stroke="var(--ink)" stroke-width="4"/>
      <path d="M30 24 l7 -3 5 11 -5 4 c2 6 6 11 12 14 l4 -5 11 5 -3 7 c-3 3 -9 3 -15 0 c-9 -5 -16 -13 -19 -22 c-2 -5 0 -9 3 -11z" fill="var(--ink)"/>
    </svg>
  </div>

  <div class="contact-divider"></div>

  <ul class="contact-list">
    <li class="contact-item contact-email">DAshcombeJR@Mailbox.com</li>
    <li class="contact-item contact-handle">_Kestrel_Rehab_</li>
    <li class="contact-item contact-web">www.KestrelRehab.com</li>
    <li class="contact-item contact-phone">555-014-2287</li>
  </ul>

  <ul class="services">
    <li class="service service-a">Brief Desc</li>
    <li class="service service-b">General Contractor</li>
    <li class="service service-c">Home Remodel</li>
    <li class="service service-d">Cocrete Alternative</li>
  </ul>
</main>
</body>
</html>
```